Bref créative
Valtoni Building and Design Stationary
Valtoni Building & Design
Professional
Martin K. Valtoni
President / Owner
4172 Wexmoor Avenue
Suite 2807
Brennmoor Falls, QX 07319
mkvaltoni@valtonibuilding.example
www.valtonibuilding.example
The logo, which will be uploaded.
Logo for the back of card. Please show us versions with both black background and white background.
Logo with white background. Please show us versions for back of card with both black and white background.

```html
<!DOCTYPE html>
<html lang="en">
<head>
<meta charset="utf-8">
<title>Valtoni Building &amp; Design – Business Cards</title>
<link rel="stylesheet" href="https://fonts.googleapis.com/css2?family=Open+Sans:wght@400;600;700&family=Cinzel:wght@400&display=swap">
<style>
  :root{
    --stage:#ece6dd;
    --card-dark:#1d1b1b;
    --card-light:#ffffff;
    --accent:#b5281f;
    --text-dark:#555555;
    --text-light:#bdbdbd;
    --caption:#2e2a26;
    --rule-dark:#4a4646;
    --rule-light:#d8d8d8;
  }
  *{box-sizing:border-box;margin:0;padding:0}
  html,body{width:1200px;height:821px;overflow:hidden}
  body{background:var(--stage);font-family:"Open Sans",Arial,sans-serif;position:relative}
  .card{position:absolute;width:500px;height:296px;border-radius:22px;box-shadow:0 3px 10px rgba(0,0,0,.18)}
  .card--dark{background:var(--card-dark)}
  .card--light{background:var(--card-light)}
  .pos-a{left:75px;top:45px}
  .pos-b{left:625px;top:45px}
  .pos-c{left:75px;top:425px}
  .pos-d{left:625px;top:425px}

  .brand{position:absolute;display:flex;flex-direction:column;align-items:center;font-weight:700;color:var(--accent);text-align:center;line-height:1.05}
  .brand__mark{width:16px;height:16px;background:var(--accent);margin-bottom:10px}
  .brand__name{font-size:38px;letter-spacing:.5px}
  .brand__sub{font-size:14px;margin-top:4px;white-space:nowrap}
  .front .brand{left:18px;top:96px;width:222px}
  .back .brand{left:0;right:0;top:92px}
  .back .brand__name{font-size:44px}
  .back .brand__sub{font-size:17px}

  .divider{position:absolute;left:248px;top:34px;width:1px;height:142px}
  .card--dark .divider{background:var(--rule-dark)}
  .card--light .divider{background:var(--rule-light)}

  .details{position:absolute;left:262px;top:34px;width:228px;font-size:10.5px;line-height:1.45}
  .details__name{color:var(--accent);font-size:15px;font-weight:400}
  .details__title{font-size:11px;margin-bottom:12px}
  .card--dark .details__title,.card--dark .details__row{color:var(--text-light)}
  .card--light .details__title,.card--light .details__row{color:var(--text-dark)}
  .details__row{display:flex;align-items:flex-start;gap:6px;margin-bottom:4px;white-space:nowrap}
  .details__row svg{flex:none;margin-top:3px}
  .details__lines{display:flex;flex-direction:column}

  .caption{position:absolute;width:500px;text-align:center;font-family:"Cinzel",Georgia,serif;font-size:19px;letter-spacing:3px;color:var(--caption)}
  .cap-a{left:75px;top:356px}
  .cap-b{left:625px;top:356px}
  .cap-c{left:75px;top:738px}
  .cap-d{left:625px;top:738px}
</style>
</head>
<body>

<section class="card card--dark front pos-a">
  <div class="brand"><span class="brand__mark"></span><span class="brand__name">Valtoni</span><span class="brand__sub">BUILDING &amp; DESIGN</span></div>
  <div class="divider"></div>
  <div class="details">
    <p class="details__name">Martin K. Valtoni</p>
    <p class="details__title">President / Owner</p>
    <div class="details__row"><svg width="9" height="11" viewBox="0 0 9 11"><path d="M4.5 0A4 4 0 0 0 .5 4c0 3 4 7 4 7s4-4 4-7a4 4 0 0 0-4-4z" fill="#b5281f"/><circle cx="4.5" cy="4" r="1.5" fill="#1d1b1b"/></svg><span class="details__lines"><span>4172 Wexmoor Avenue</span><span>Suite 2807</span><span>Brennmoor Falls, QX 07319</span></span></div>
    <div class="details__row"><svg width="9" height="9" viewBox="0 0 9 9"><rect x="2" y="0" width="5" height="9" rx="1" fill="#b5281f"/></svg><span>555-014-0148</span></div>
    <div class="details__row"><svg width="9" height="9" viewBox="0 0 9 9"><rect x="0" y="1.5" width="9" height="6" fill="#b5281f"/><path d="M0 1.5l4.5 3.5 4.5-3.5" stroke="#1d1b1b" fill="none"/></svg><span>mkvaltoni@valtonibuilding.example</span></div>
    <div class="details__row"><svg width="9" height="9" viewBox="0 0 9 9"><circle cx="4.5" cy="4.5" r="4.5" fill="#b5281f"/></svg><span>www.valtonibuilding.example</span></div>
  </div>
</section>
<p class="caption cap-a">Business Card Option A</p>

<section class="card card--light front pos-b">
  <div class="brand"><span class="brand__mark"></span><span class="brand__name">Valtoni</span><span class="brand__sub">BUILDING &amp; DESIGN</span></div>
  <div class="divider"></div>
  <div class="details">
    <p class="details__name">Martin K. Valtoni</p>
    <p class="details__title">President / Owner</p>
    <div class="details__row"><svg width="9" height="11" viewBox="0 0 9 11"><path d="M4.5 0A4 4 0 0 0 .5 4c0 3 4 7 4 7s4-4 4-7a4 4 0 0 0-4-4z" fill="#b5281f"/><circle cx="4.5" cy="4" r="1.5" fill="#fff"/></svg><span class="details__lines"><span>4172 Wexmoor Avenue</span><span>Suite 2807</span><span>Brennmoor Falls, QX 07319</span></span></div>
    <div class="details__row"><svg width="9" height="9" viewBox="0 0 9 9"><rect x="2" y="0" width="5" height="9" rx="1" fill="#b5281f"/></svg><span>555-014-0148</span></div>
    <div class="details__row"><svg width="9" height="9" viewBox="0 0 9 9"><rect x="0" y="1.5" width="9" height="6" fill="#b5281f"/><path d="M0 1.5l4.5 3.5 4.5-3.5" stroke="#fff" fill="none"/></svg><span>mkvaltoni@valtonibuilding.example</span></div>
    <div class="details__row"><svg width="9" height="9" viewBox="0 0 9 9"><circle cx="4.5" cy="4.5" r="4.5" fill="#b5281f"/></svg><span>www.valtonibuilding.example</span></div>
  </div>
</section>
<p class="caption cap-b">Business Card Option B</p>

<section class="card card--dark back pos-c">
  <div class="brand"><span class="brand__mark"></span><span class="brand__name">Valtoni</span><span class="brand__sub">BUILDING &amp; DESIGN</span></div>
</section>
<p class="caption cap-c">Business Card Back</p>

<section class="card card--light back pos-d">
  <div class="brand"><span class="brand__mark"></span><span class="brand__name">Valtoni</span><span class="brand__sub">BUILDING &amp; DESIGN</span></div>
</section>
<p class="caption cap-d">Business Card Back</p>

</body>
</html>
```